COMPANY NAME: Bright Harbor Outlooks: Task Description: We are a new UK based business with global rea

Target Market

- Personal and professional development – 30-55 age group, corporate leaders, Eastern European and Asian markets
- On-assignment projects – Corporate market – Eastern European and Asian Markets
- Property investment - 35-65 age group, Europe, USA, Australia

What we need

We need logos and brand design for a suite of web platforms (website, twitter and Facebook profile). We would like to have a cohesive and consistent look across all of our online platforms. The design suite must therefore include social media logos, backgrounds and headers. Specifically we are looking for:

a. Facebook header/page design: likely to have a more youthful look

b. Website: Header, background and layout that is responsive to devices, iPhone primarily, then tablet, then PC (we have purchased a website building package from WebNimbus so if you are familiar with one of their themes, it would be great to have a design that fits with a theme you would recommend); Design should be able to accommodate a place to position video in the medium term but an image in the short term.

c. LinkedIn: header/logo; more corporate look

d. Twitter: background/logo

e. Powerpoint template: background and logo - simple and soft background not busy

f. Electronic Newsletter: logo, header and sidebar; simple and soft background not busy

h. Business card: sophisticated and simple

Colors

We have in mind a preference for colors from the purple family, maybe lavender, so as to appeal to all genders and age groups. Though we are happy to go with a recommendation if you think otherwise.

We would like a look that is professional, airy, bright, fresh, futuristic, insightful, friendly.

Ethos of the brand

- experiencing opportunity and being fulfilled in a changing world
- services are facilitated through insights
- support provided through our product, services and tailored approach to coaching/partnerships (which includes private client match-making)
- we are service providers and passionate about quality and modern leadership skills at all stages in life.

The company name is "Bright Harbor Outlooks” - our main message is helping people move to the next level - through investments, personal and professional growth.

Some of our messaging

1. International Leadership in a new world.

2. New technology;

3. Informed;

4. Positively Influential

5. Making a difference;

6. Empowered;

7. Risk free investments;

8. Commercial opportunity;

9. Fulfilled living;

10. Carefree and Fun Living;

11. Progression;

12. Open-minded

13. Energy/dynamic

The Business:
The business is to move people very quickly out of situations that hold them back. the situations could be their own personal situations; their career; their jobs; their teams; their ideas; their finances; their financial opportunities. Remove their fears and give them the strategies to take action. The team are international and have 40 years experience between them in this area.

We do want to come across modern and dynamic, customer outcome focussed, building long-term relationships; international.
Updates

Project Deadline Extended
Reason: We have not found the right designs - we are not just looking for a website design but also images and logos. Most images we can see in the designs are stock images - very standard. We need an image which will be the face of the company, like the shop front window. This main image will be used on social media (top image) and also the home page of the website.

Target Market(s)

30-55 years
Eastern Europe; UK; Asia; Africa; Middle East
Personal, Professional, Corporate, and Financial Growth

Industry/Entity Type

Business Service

Contact Information for Business Card

Simple and stylish
the 3 areas of the business on the reverse -

International look - Offices in UK and San Francisco

Company name
web address www.brightharboroutlook.example
email director@brightharboroutlook.example
Facebook bright harbor outlook
LinkedIn Bright Harbor Outlook
Twitter Bright Harbor Outlook
Telephone: +44 (0) 700 900 0123

Logo Text

Something that symbolises unlimited growth - probably not text - could use the word INSIGHT in some way

Number of Pages Required

1 page

Colors
e4daeb
f3f1f8
ffffff

Requirements
Must have
• social media symbols and address
• company name
• Marianne Tolley
• Director
• Telephone +44 (0) 700 900 0123
• Website name www.brightharboroutlook.example.uk
• Reverse of Card:
• Discreet, Fast, Bright Harbor Consultancy
• Corporate, Professional, Personal & Property Investment
Nice to have
• not too angular; soft lines; not too cluttered (possibly social media on the reverse and just logo, name, number on the front?
Should not have
• too busy

```html
<!DOCTYPE html>
<html lang="en">
<head>
<meta charset="utf-8">
<title>Bright Harbor Outlook — Home</title>
<link rel="stylesheet" href="https://fonts.googleapis.com/css2?family=Questrial&family=Raleway:wght@400;500;600;700&family=Open+Sans:ital,wght@0,400;0,600;1,400&display=swap">
<style>
  :root {
    --white: #ffffff;
    --ink: #2b2b2b;
    --ink-soft: #555555;
    --muted: #7d7d7d;
    --lavender: #e9e3ef;
    --lavender-pale: #f4f3f9;
    --lavender-footer: #efeaf3;
    --accent: #b48ac7;
    --star: #f5a623;
    --pager-active: #1a9bd7;
    --pager: #c3c3c8;
  }
  * { margin: 0; padding: 0; box-sizing: border-box; }
  html, body { width: 1200px; height: 2190px; overflow: hidden; background: var(--white); }
  body { position: relative; font-family: "Open Sans", sans-serif; color: var(--ink); }
  h1, h2, h3 { font-weight: 400; }

  /* Header */
  .site-header { position: absolute; left: 0; top: 0; width: 1200px; height: 88px; background: var(--white); box-shadow: 0 2px 6px rgba(0,0,0,.08); z-index: 3; }
  .brand { position: absolute; left: 142px; top: 28px; font-family: "Questrial", sans-serif; font-size: 28px; color: #111; white-space: nowrap; }
  .main-nav { position: absolute; left: 464px; top: 35px; display: flex; gap: 22px; font-family: "Raleway", sans-serif; font-size: 15.5px; color: var(--ink-soft); }

  /* Hero */
  .hero { position: absolute; left: 0; top: 88px; width: 1200px; height: 540px; overflow: hidden; }
  .hero-photo {
    position: absolute; inset: 0;
    background:
      radial-gradient(ellipse 260px 200px at 240px 110px, rgba(250,250,252,.95), rgba(250,250,252,0) 70%),
      radial-gradient(ellipse 200px 240px at 650px 330px, rgba(40,48,72,.85), rgba(40,48,72,0) 72%),
      radial-gradient(ellipse 170px 170px at 610px 130px, rgba(214,176,138,.75), rgba(214,176,138,0) 70%),
      radial-gradient(ellipse 260px 330px at 980px 330px, rgba(112,132,180,.95), rgba(112,132,180,0) 72%),
      radial-gradient(ellipse 170px 150px at 870px 120px, rgba(120,88,70,.6), rgba(120,88,70,0) 70%),
      radial-gradient(ellipse 420px 120px at 520px 520px, rgba(246,246,248,.95), rgba(246,246,248,0) 75%),
      radial-gradient(ellipse 180px 140px at 330px 440px, rgba(150,150,158,.7), rgba(150,150,158,0) 72%),
      linear-gradient(100deg, #e9e9ec 0%, #dedcdf 30%, #d0cbce 50%, #b9bfcf 70%, #a3afca 85%, #dadce2 100%);
  }
  .hero-caption { position: absolute; left: 117px; top: 220px; width: 448px; height: 136px; background: rgba(233,226,238,.88); }
  .hero-caption h1 { position: absolute; left: 41px; top: 24px; font-family: "Questrial", sans-serif; font-weight: 700; font-size: 37px; color: #1b1b1b; white-space: nowrap; }
  .hero-caption p { position: absolute; left: 41px; top: 76px; font-family: "Questrial", sans-serif; font-weight: 700; font-size: 22px; color: #1b1b1b; white-space: nowrap; }
  .hero-edge { position: absolute; left: 0; top: 480px; }
  .hero-dots { position: absolute; left: 550px; top: 506px; }

  /* About */
  .about-title { position: absolute; left: 148px; top: 690px; font-family: "Raleway", sans-serif; font-size: 31px; color: #333; }
  .about-copy { position: absolute; left: 149px; top: 745px; width: 450px; font-size: 13.5px; line-height: 23.5px; color: var(--ink-soft); }
  .about-copy p { margin-bottom: 7px; }
  .video { position: absolute; left: 676px; top: 673px; width: 379px; height: 244px; border: 1px solid #9aa; overflow: hidden; }
  .video-frame { position: absolute; inset: 0;
    background:
      radial-gradient(ellipse 90px 80px at 230px 110px, rgba(60,90,140,.7), rgba(60,90,140,0) 70%),
      radial-gradient(ellipse 80px 70px at 110px 150px, rgba(70,100,150,.6), rgba(70,100,150,0) 70%),
      linear-gradient(120deg, #8fa3b8 0%, #c6d2dc 40%, #6d86a4 70%, #a8b6c6 100%); }
  .video svg { position: absolute; left: 0; top: 0; }

  /* Services */
  .services { position: absolute; left: 0; top: 964px; width: 1200px; height: 328px; background: var(--lavender); }
  .service-icon { position: absolute; width: 128px; height: 128px; border-radius: 50%; background: var(--white); border: 1px solid #ddd6e2; }
  .service-icon svg { position: absolute; left: 34px; top: 34px; }
  .service h2 { position: absolute; font-family: "Raleway", sans-serif; font-weight: 500; font-size: 22px; color: #333; }
  .service ul { position: absolute; list-style: none; font-size: 14.5px; line-height: 27.5px; color: var(--muted); }
  .btn-more { position: absolute; width: 112px; height: 35px; border: 1px solid #777; background: var(--white); font-size: 12.5px; letter-spacing: .6px; color: #333; text-align: center; line-height: 33px; }

  /* Testimonials */
  .testimonials { position: absolute; left: 0; top: 1295px; width: 1200px; height: 413px; background: var(--lavender-pale); }
  .section-title { font-family: "Raleway", sans-serif; font-weight: 400; font-size: 30px; color: #333; }
  .testimonials .section-title { position: absolute; left: 0; width: 1200px; top: 58px; text-align: center; }
  .t-card { position: absolute; top: 150px; width: 294px; height: 189px; background: var(--white); border: 1px solid #dedde3; }
  .t-avatar { position: absolute; left: 112px; top: -36px; width: 70px; height: 70px; border-radius: 50%; border: 3px solid #e4e4ea; }
  .t-name { position: absolute; left: 0; width: 100%; top: 43px; text-align: center; font-size: 14.5px; color: #222; }
  .t-quote { position: absolute; left: 22px; right: 22px; top: 68px; text-align: center; font-style: italic; font-size: 12px; line-height: 19.5px; color: var(--muted); }
  .t-stars { position: absolute; left: 0; width: 100%; top: 158px; text-align: center; }
  .pager { position: absolute; left: 562px; top: 365px; display: flex; gap: 6px; }
  .pager span { width: 30px; height: 4px; background: var(--pager); }
  .pager span.active { background: var(--pager-active); }

  /* News */
  .news .section-title { position: absolute; left: 145px; top: 1768px; }
  .news-item { position: absolute; top: 1830px; width: 290px; }
  .news-item h3 { font-family: "Raleway", sans-serif; font-size: 18px; color: #555; margin-bottom: 10px; }
  .news-item p { font-size: 12.5px; line-height: 23.5px; color: var(--muted); }
  .news-item .read-more { display: block; margin-top: 12px; font-size: 12.5px; letter-spacing: .3px; color: #222; }

  /* Footer */
  .site-footer { position: absolute; left: 0; top: 2041px; width: 1200px; height: 149px; background: var(--lavender-footer); }
  .footer-nav { position: absolute; left: 146px; top: 32px; display: flex; gap: 19px; font-family: "Raleway", sans-serif; font-size: 15.5px; color: #333; }
  .legal { position: absolute; left: 146px; top: 66px; font-size: 11.5px; color: #444; }
  .contact { position: absolute; left: 830px; top: 28px; font-size: 13.5px; color: #222; line-height: 29px; }
  .contact div { display: flex; align-items: center; gap: 8px; }
  .social { position: absolute; left: 834px; top: 94px; display: flex; gap: 28px; }
  .social span { width: 16px; height: 16px; border-radius: 50%; background: var(--accent); }
</style>
</head>
<body>

<header class="site-header">
  <div class="brand">Bright Harbor Outlook</div>
  <nav class="main-nav">
    <span>About You</span><span>About Us</span><span>Our Values</span><span>Testimonials</span><span>Social Media</span><span>News Alert</span>
  </nav>
</header>

<section class="hero">
  <div class="hero-photo" role="img" aria-label="Signature hero photo: consultant with glasses advising a client at a bright office desk with a laptop"></div>
  <div class="hero-caption">
    <h1>Consultancy Services</h1>
    <p>Morbi diam mauris viverr</p>
  </div>
  <svg class="hero-edge" width="1200" height="60" viewBox="0 0 1200 60">
    <polygon points="0,9 600,57 1200,9 1200,60 0,60" fill="#ffffff"/>
  </svg>
  <svg class="hero-dots" width="100" height="22" viewBox="0 0 100 22">
    <circle cx="9" cy="11" r="7.5" fill="#fff" stroke="#111" stroke-width="2"/>
    <circle cx="30" cy="11" r="8.5" fill="#111"/>
    <circle cx="50" cy="11" r="8.5" fill="#111"/>
    <circle cx="70" cy="11" r="8.5" fill="#111"/>
  </svg>
</section>

<section class="about">
  <h2 class="about-title">About Bright Harbor Outlook</h2>
  <div class="about-copy">
    <p>Hello and welcome to the company that works with you on your terms.</p>
    <p>If you seek an experienced and trusted partner to work with you on an assignment or simply want some strategies to move your personal or professional talents to the next level then you are in the right place.</p>
    <p>If you feel that the pace of change in business is so fast that to be an outstanding leader you should ensure you</p>
  </div>
  <div class="video">
    <div class="video-frame" role="img" aria-label="Video still: team gathered around a laptop in a meeting"></div>
    <svg width="379" height="244" viewBox="0 0 379 244">
      <circle cx="187" cy="118" r="24" fill="rgba(0,0,0,.15)" stroke="#fff" stroke-width="3"/>
      <polygon points="180,105 180,131 200,118" fill="#fff"/>
      <rect x="0" y="210" width="379" height="34" fill="#2a2a2e"/>
      <polygon points="14,220 14,232 24,226" fill="#fff"/>
      <rect x="32" y="224" width="300" height="5" rx="2.5" fill="#ddd"/>
      <rect x="32" y="224" width="102" height="5" rx="2.5" fill="#3b7fd0"/>
      <polygon points="347,223 351,223 356,219 356,233 351,229 347,229" fill="#fff"/>
      <path d="M359,222 q4,4 0,8" stroke="#fff" stroke-width="1.5" fill="none"/>
    </svg>
  </div>
</section>

<section class="services">
  <div class="service">
    <div class="service-icon" style="left:159px;top:84px;">
      <svg width="60" height="60" viewBox="0 0 60 60" fill="none" stroke="#333" stroke-width="2.4">
        <rect x="2" y="6" width="22" height="14" rx="2"/>
        <path d="M8 20 l-2 6 l7 -6"/>
        <circle cx="8" cy="13" r="1" fill="#333"/><circle cx="13" cy="13" r="1" fill="#333"/><circle cx="18" cy="13" r="1" fill="#333"/>
        <circle cx="38" cy="20" r="9"/>
        <path d="M20 56 v-8 q0 -12 18 -12 q18 0 18 12 v8 z"/>
      </svg>
    </div>
    <h2 style="left:301px;top:86px;">CONSULTANCY</h2>
    <ul style="left:301px;top:117px;">
      <li>Professional and Personal</li>
      <li>Next Generation Leaders (16-30)</li>
      <li>Consultation Options</li>
    </ul>
    <div class="btn-more" style="left:300px;top:219px;">MORE INFO</div>
  </div>
  <div class="service">
    <div class="service-icon" style="left:620px;top:84px;">
      <svg width="60" height="60" viewBox="0 0 60 60" fill="#444">
        <rect x="4" y="6" width="22" height="22"/>
        <rect x="30" y="6" width="22" height="22"/>
        <rect x="4" y="32" width="22" height="22"/>
        <rect x="34" y="36" width="18" height="18" transform="rotate(20 43 45)"/>
      </svg>
    </div>
    <h2 style="left:758px;top:86px;">ON ASSIGNMENT</h2>
    <ul style="left:762px;top:117px;">
      <li>Team Cohesion Strategy</li>
      <li>Go To Market Strategy</li>
      <li>Internationalisation Strategy</li>
    </ul>
    <div class="btn-more" style="left:761px;top:219px;">MORE INFO</div>
  </div>
</section>

<section class="testimonials">
  <h2 class="section-title">Testimonials</h2>

  <article class="t-card" style="left:159px;">
    <div class="t-avatar" role="img" aria-label="Client portrait" style="background:linear-gradient(160deg,#d9a07f,#8c4a35);"></div>
    <div class="t-name">Julies Aenderson</div>
    <p class="t-quote">Morbi diam mauris viverra in gravida eu mattis in ante Morbi eget arcu Morbi porta libero id ullamcorper nonummy nibh ligula pulvinar metus consectetuer</p>
    <div class="t-stars"><svg width="72" height="16" viewBox="0 0 72 16"><g fill="#f5a623"><polygon id="st" points="8,0 10.4,5.2 16,5.8 11.8,9.6 13,15.2 8,12.4 3,15.2 4.2,9.6 0,5.8 5.6,5.2"/><use href="#st" x="18"/><use href="#st" x="36"/><use href="#st" x="54"/></g></svg></div>
  </article>

  <article class="t-card" style="left:466px;">
    <div class="t-avatar" role="img" aria-label="Client portrait" style="background:linear-gradient(160deg,#e8c2a4,#9c6b4e);"></div>
    <div class="t-name">Mark Wog</div>
    <p class="t-quote">Suspendisse risus nibh ultricies eu volut-pat non condimentum hendrerit augue Etiam eleifend metus vitae</p>
    <div class="t-stars"><svg width="72" height="16" viewBox="0 0 72 16"><g fill="#f5a623"><use href="#st" x="0"/><use href="#st" x="18"/><use href="#st" x="36"/><use href="#st" x="54"/></g></svg></div>
  </article>

  <article class="t-card" style="left:769px;">
    <div class="t-avatar" role="img" aria-label="Client portrait" style="background:linear-gradient(160deg,#f1e2c6,#c8a277);"></div>
    <div class="t-name">Susan</div>
    <p class="t-quote">Curabitur vel mi sit amet magna malesuada ultrices Ut nisi erat fermentum vel congue id euismod in elit Fusce ultricies orci ac</p>
    <div class="t-stars"><svg width="72" height="16" viewBox="0 0 72 16"><g fill="#f5a623"><use href="#st" x="0"/><use href="#st" x="18"/><use href="#st" x="36"/><use href="#st" x="54"/></g></svg></div>
  </article>

  <div class="pager"><span></span><span class="active"></span><span></span></div>
</section>

<section class="news">
  <h2 class="section-title">News Alerts</h2>
  <article class="news-item" style="left:145px;">
    <h3>Praesent elementum elit</h3>
    <p>at tellus nec ultricies sit amet porttitor mattis enim In massa libero interdum malesuada ultrices Ut nisi erat fermentum</p>
    <span class="read-more">READ MORE</span>
  </article>
  <article class="news-item" style="left:464px;">
    <h3>Nullam enim leo egestas</h3>
    <p>at tellus nec ultricies sit amet porttitor mattis enim In massa libero interdum malesuada ultrices Ut nisi erat fermentum</p>
    <span class="read-more">READ MORE</span>
  </article>
  <article class="news-item" style="left:783px;">
    <h3>Curabitur tristique</h3>
    <p>at tellus nec ultricies sit amet porttitor mattis enim In massa libero interdum malesuada ultrices Ut nisi erat fermentum</p>
    <span class="read-more">READ MORE</span>
  </article>
</section>

<footer class="site-footer">
  <nav class="footer-nav">
    <span>About You</span><span>About Us</span><span>Our Values</span><span>Testimonials</span><span>Social Media</span><span>News Alert</span>
  </nav>
  <div class="legal">© 2016 Company Name &nbsp;All right reserved &nbsp;Term of Use</div>
  <div class="contact">
    <div>
      <svg width="16" height="12" viewBox="0 0 16 12"><rect width="16" height="12" rx="1.5" fill="#b48ac7"/><path d="M1 1 l7 6 l7 -6" stroke="#fff" stroke-width="1.4" fill="none"/></svg>
      Director@brightharboroutlook.example
    </div>
    <div>
      <svg width="16" height="16" viewBox="0 0 16 16"><path d="M3 1 l3 0 l1.5 4 l-2 1.5 q1.5 3 4 4 l1.5 -2 l4 1.5 l0 3 q-1 1.5 -3 1.5 q-6 -1 -10 -8 q-1 -3 1 -5.5z" fill="#b48ac7"/></svg>
      +44 (0) 700 900 0123
    </div>
  </div>
  <div class="social" aria-label="Social media links">
    <span></span><span></span><span></span><span></span><span></span>
  </div>
</footer>

</body>
</html>
```